High-end construction company needs a business card design

We need a modern looking business card that draws people in, is memorable and looks so good people will want to sick it on their fridges.
On the first side what is needed are:
Logo
My name - Tomas Verbelk
Title - Managing Director
Website - www.kravel.co.uk
Email - tomas@kravel.co.uk
Telephone - 020 5194 6381
Mobile - 07845319027
On the back side was is needed is a list of all the services we provide:
-Kitchen Renovations
-Bathroom Renovations
-House Renovations
-Garage Conversions
-Extensions
-Loft Conversions
-Conservatories
-Carpentry
-Tiling
-Electrical
-Plumbing & Heating
-Bricklaying
-Landscaping
-Decorating
-Plastering
We would like the colours to be the same shades as on the logo with grey or black for the words.
Target Market(s)
Anyone who needs building work done
Contact Information for Business Card
This business card is for a construction company which strives to deliver excellent service and quality.
The look and feel of the card should represent this.
Requirements
Must have
- On the first side what is needed are:
Logo
My name - Tomas Verbelk
Title - Managing Director
Website - www.kravel.co.uk
Email - tomas@kravel.co.uk
Telephone - 020 5194 6381
Mobile - 07845319027
Nice to have
- Cool looking features

```html
<!DOCTYPE html>
<html lang="en">
<head>
<meta charset="utf-8">
<title>Kravel Construction Ltd – Business Card</title>
<link rel="stylesheet" href="https://fonts.googleapis.com/css2?family=Questrial&family=Montserrat:wght@600;700&display=swap">
<style>
  :root {
    --backdrop: #033b5f;
    --green: #5fa459;
    --green-deep: #4f9a4a;
    --green-bright: #7dc443;
    --paper: #ffffff;
    --mist: #e9eaea;
    --mist-dark: #d6d8d8;
    --ink: #6b6b6b;
    --white: #ffffff;
  }
  * { box-sizing: border-box; margin: 0; padding: 0; }
  html, body { width: 1200px; height: 1200px; overflow: hidden; }
  body {
    background: var(--backdrop);
    font-family: "Questrial", "Century Gothic", sans-serif;
    display: flex;
    align-items: center;
    justify-content: center;
    gap: 60px;
  }
  .card {
    position: relative;
    width: 460px;
    height: 710px;
    overflow: hidden;
    box-shadow: 0 18px 40px rgba(0,0,0,0.35);
  }
  .card__curve { position: absolute; left: 0; top: 0; width: 100%; height: 100%; }

  /* Front */
  .card--front { background: var(--green); }
  .site-photo {
    position: absolute; left: 0; top: 0; width: 100%; height: 330px;
    background: linear-gradient(180deg, #f4f4f4 0%, var(--mist) 55%, var(--mist-dark) 100%);
  }
  .brand {
    position: absolute; left: 0; width: 100%;
    text-align: center;
    font-family: "Montserrat", sans-serif;
    font-weight: 700;
    line-height: 1;
  }
  .brand__name { display: block; font-size: 62px; letter-spacing: 3px; }
  .brand__sub { display: block; font-size: 15px; letter-spacing: 3px; margin-top: 10px; }
  .brand__mark { display: inline-block; width: 16px; height: 16px; margin-bottom: 14px; }
  .card--front .brand { top: 120px; color: var(--green); }
  .card--front .brand__mark { background: var(--green); }

  .holder {
    position: absolute; left: 0; top: 405px; width: 100%;
    text-align: center; color: var(--white);
  }
  .holder__name {
    font-family: "Montserrat", sans-serif; font-weight: 600;
    font-size: 30px; letter-spacing: 1px; text-transform: uppercase;
  }
  .holder__title { font-size: 19px; margin-top: 4px; opacity: 0.95; }
  .divider {
    width: 260px; height: 1px; margin: 20px auto;
    background: linear-gradient(90deg, transparent, rgba(255,255,255,0.9), transparent);
  }
  .contact { font-size: 21px; line-height: 1.6; }

  /* Back */
  .card--back { background: var(--paper); }
  .card--back .brand { top: 95px; color: var(--white); }
  .card--back .brand__mark { background: var(--white); }
  .services {
    position: absolute; left: 0; top: 345px; width: 100%;
    text-align: center; color: var(--ink);
  }
  .services__heading {
    font-family: "Montserrat", sans-serif; font-weight: 700;
    color: var(--green-deep); font-size: 20px; letter-spacing: 1px;
  }
  .services__rule { width: 190px; height: 1px; background: var(--mist-dark); margin: 10px auto 14px; }
  .services__list { list-style: none; font-size: 18px; line-height: 1.72; }
</style>
</head>
<body>

  <section class="card card--front" aria-label="Card front">
    <div class="site-photo" role="img" aria-label="Faint photograph of a construction site with tower cranes"></div>
    <svg class="card__curve" viewBox="0 0 460 710" preserveAspectRatio="none" aria-hidden="true">
      <path d="M0 290 Q230 390 460 290 L460 0 L0 0 Z" fill="transparent"/>
      <path d="M0 290 Q230 380 460 250 L460 0 L0 0 Z" fill="#e6e7e7"/>
      <path d="M0 290 Q230 380 460 250" fill="none" stroke="var(--green-bright)" stroke-width="6"/>
    </svg>
    <div class="brand">
      <span class="brand__mark"></span>
      <span class="brand__name">KRAVEL</span>
      <span class="brand__sub">CONSTRUCTION LTD</span>
    </div>
    <div class="holder">
      <h1 class="holder__name">Tomas Verbelk</h1>
      <p class="holder__title">Managing Director</p>
      <div class="divider"></div>
      <p class="contact">T: 020 5194 6381<br>M: 07845319027</p>
      <div class="divider"></div>
      <p class="contact">W: www.kravel.co.uk<br>E: tomas@kravel.co.uk</p>
    </div>
  </section>

  <section class="card card--back" aria-label="Card back">
    <svg class="card__curve" viewBox="0 0 460 710" preserveAspectRatio="none" aria-hidden="true">
      <path d="M0 0 L460 0 L460 200 Q300 330 0 300 Z" fill="var(--green)"/>
      <path d="M0 300 Q300 330 460 200" fill="none" stroke="var(--green-bright)" stroke-width="6"/>
    </svg>
    <div class="brand">
      <span class="brand__mark"></span>
      <span class="brand__name">KRAVEL</span>
      <span class="brand__sub">CONSTRUCTION LTD</span>
    </div>
    <div class="services">
      <h2 class="services__heading">WE PROVIDE</h2>
      <div class="services__rule"></div>
      <ul class="services__list">
        <li>Kitchen Renovations</li>
        <li>Bathroom Renovations</li>
        <li>House Renovations</li>
        <li>Garage Conversions | Extensions</li>
        <li>Loft Conversions | Conservatories</li>
        <li>Carpentry | Tiling | Electrical</li>
        <li>Plumbing &amp; Heating | Bricklaying</li>
        <li>Landscaping</li>
        <li>Decorating | Plastering</li>
      </ul>
    </div>
  </section>

</body>
</html>
```